Modern, professional flyer for a Painting & decorating company. I would like to include my lo...

I run a small painting and decorating company that covers central and North London areas. I have a small crew of 3 painters that are all very experienced and have been painting for a least 20 years. We pride ourselves on being very efficient, friendly and carrying out work at an affordable cost.
I would like to include the different tasks we can carry out such as; Interior and exterior painting, residential, comercial and industrial jobs. Wallpaper hanging/ removal, filling and plastering. I would like also to include that I am on Fixaroster and have a current rating of 9.77. I'm also on Trusted Folk where if needed they can go and visit to look at past work and ratings.
I would like to keep the general outlook of the flyer simplistic as too much wording in my opinion puts people off reading it.

Target Market(s)

Local residential houses, shops, businesses etc.

Industry/Entity Type

Painting And Decorating

Colors

Designer to choose colors to be used in the design.

Requirements
Must have
• Size A5 Double sided.
• Contact Details
• Mobile 07846 203958
• Email: brushloft@mailvane.com

```html
<!DOCTYPE html>
<html lang="en">
<head>
<meta charset="utf-8">
<title>Brush Loft – Painting &amp; Decorating Flyer</title>
<link rel="stylesheet" href="https://fonts.googleapis.com/css2?family=Cinzel:wght@400;500&display=swap">
<style>
  :root {
    --ink: #1b1b1b;
    --ochre: #f5ae35;
    --ochre-deep: #e99c22;
    --stone: #c4c4c4;
    --paper: #ffffff;
    --rule: #8a8a8a;
  }
  * { margin: 0; padding: 0; box-sizing: border-box; }
  html, body {
    width: 1200px; height: 851px; overflow: hidden;
    background: var(--ink);
    font-family: "Cinzel", Georgia, serif;
  }
  .spread { position: relative; width: 1200px; height: 851px; }
  .page { position: absolute; top: 0; height: 851px; background: var(--ink); overflow: hidden; }
  .page--front { left: 0; width: 600px; }
  .page--back { left: 601px; width: 599px; }
  .fold { position: absolute; left: 600px; top: 0; width: 1px; height: 851px; background: var(--rule); }

  /* Front */
  .brand-name {
    position: absolute; left: 0; width: 600px; top: 290px;
    text-align: center; color: var(--stone);
    font-size: 44px; font-weight: 500; letter-spacing: 1px;
    font-variant: small-caps;
  }
  .brush-sweep {
    position: absolute; left: 94px; top: 362px; width: 422px; height: 60px;
    border-radius: 40px 60px 60px 30px;
    background: linear-gradient(90deg, #f4f4f4 0%, #e6e6e6 45%, #6a6a6a 80%, rgba(27,27,27,0) 100%);
  }
  .contact {
    position: absolute; left: 0; width: 600px; top: 428px;
    text-align: center; color: var(--stone); font-size: 22px; line-height: 26px;
  }
  .contact-label { letter-spacing: 8px; font-size: 20px; }
  .ratings-band {
    position: absolute; left: 0; top: 555px; width: 600px; height: 17px;
    background: var(--paper); color: var(--ink);
    font-size: 13px; line-height: 17px; white-space: nowrap; padding-left: 22px;
  }
  .front-paint {
    position: absolute; left: 0; top: 572px; width: 600px; height: 279px;
    background: linear-gradient(100deg, var(--ochre-deep) 0%, var(--ochre) 30%, #f7b43e 70%, var(--ochre) 100%);
  }

  /* Back */
  .back-paint { position: absolute; left: 0; top: 0; }
  .frame {
    position: absolute; left: 30px; top: 41px; width: 538px; height: 790px;
    border: 34px solid var(--paper);
  }
  .services-title {
    position: absolute; left: 95px; top: 100px;
    color: var(--stone); font-size: 34px; font-weight: 500; letter-spacing: 1px;
  }
  .services-list {
    position: absolute; left: 96px; top: 168px; list-style: none;
    color: var(--stone); font-size: 20px; letter-spacing: 0.5px;
  }
  .services-list li { height: 30px; line-height: 30px; }
  .services-list li::before { content: "\00B0"; margin-right: 10px; font-size: 18px; }
  .call-out {
    position: absolute; right: 120px; top: 368px;
    color: var(--stone); font-size: 34px; font-weight: 500; letter-spacing: 1px;
  }
  .back-brand {
    position: absolute; left: 290px; top: 530px; width: 130px;
    text-align: center; color: var(--stone); font-size: 18px; font-weight: 500;
  }
</style>
</head>
<body>
<main class="spread">
  <section class="page page--front">
    <h1 class="brand-name">Brush Loft</h1>
    <div class="brush-sweep" role="img" aria-label="White dry-brush paint stroke"></div>
    <p class="contact">
      <span class="contact-label">MOBILE</span> | 07846 203958<br>
      <span class="contact-label">EMAIL</span> | BRUSHLOFT@MAILVANE.COM
    </p>
    <p class="ratings-band">&deg; FIXAROSTER RATING 9.77 &deg;&nbsp; TRUSTED FOLK &deg; FIXAROSTER RATING 9.77 &deg;</p>
    <div class="front-paint" role="img" aria-label="Broad ochre paint brush strokes"></div>
  </section>

  <div class="fold"></div>

  <section class="page page--back">
    <svg class="back-paint" width="599" height="851" viewBox="0 0 599 851" role="img" aria-label="Ochre paint brush strokes sweeping up from the bottom">
      <polygon fill="#f5ae35" points="0,470 30,490 30,851 0,851"/>
      <polygon fill="#f5ae35" points="568,560 599,545 599,851 568,851"/>
      <polygon fill="#f5ae35" points="64,360 100,345 160,470 220,620 280,700 360,650 420,540 450,515 480,560 533,580 533,795 64,795"/>
      <polygon fill="#f5ae35" points="30,831 568,831 568,851 30,851"/>
    </svg>
    <div class="frame"></div>
    <h2 class="services-title">IF YOU NEED</h2>
    <ul class="services-list">
      <li>Interior and exterior painting</li>
      <li>Residential jobs</li>
      <li>Comercial jobs</li>
      <li>Industrial jobs</li>
      <li>Wallpaper hanging/ removal</li>
      <li>Filling and plastering</li>
    </ul>
    <p class="call-out">CALL US!</p>
    <p class="back-brand">Brush Loft</p>
  </section>
</main>
</body>
</html>
```